Thermlio Energy Ratings Whole Home Energy Rating Flyer

Please create a flyer 8.5" x 11" that is 2-sided that goes hand and hand with my tri-fold flyer. The flyer will target prospective homeowners and real estate agents to purchase a whole home energy rating. I have attached further details.

Target Market(s)

Homeowners looking to remodel their homes, save on energy bills, purchase or sell a home.

Font styles to use
Serif
Sans Serif

Colors
3176b5
ffffff

Requirements
Must have
• Must be able to sell a whole home energy rating on its own!
Nice to have
• I would like to mimic the colors and background of my tri-fold flyer.
Should not have
• Should not be boring!

```html
<!DOCTYPE html>
<html lang="en">
<head>
<meta charset="utf-8">
<title>Thermlio Energy Ratings – Whole Home Energy Rating Flyer</title>
<link rel="stylesheet" href="https://fonts.googleapis.com/css2?family=Poppins:wght@400;500;600;700;800&family=Lora:ital,wght@1,400&display=swap">
<style>
:root{
  --stage:#a9a9a9;
  --paper:#ffffff;
  --blue:#1d6cc2;
  --blue-deep:#1559a8;
  --navy:#2c4a6e;
  --ink:#2b2b2b;
  --ink-soft:#444;
  --rule:#cfd6df;
}
*{margin:0;padding:0;box-sizing:border-box}
html,body{width:1200px;height:1200px;overflow:hidden;background:var(--stage)}
body{position:relative;font-family:"Poppins",Arial,sans-serif;color:var(--ink)}
.page{position:absolute;top:242px;width:530px;height:686px;background:var(--paper);overflow:hidden}
.page--front{left:58px}
.page--back{left:605px}
.abs{position:absolute}

/* front */
.intro{left:36px;top:44px;width:270px;font-size:11px;line-height:13.5px;color:var(--ink-soft)}
.contact-top{left:336px;top:44px;font-weight:700;color:var(--ink)}
.contact-top .phone{font-size:10.5px;display:flex;align-items:center;gap:4px}
.contact-top .web{font-size:13.5px;display:flex;align-items:center;gap:4px;margin-top:1px}
.icon{fill:var(--blue)}
.hero{left:0;top:112px;width:530px;height:153px;background:var(--blue)}
.hero-photo{position:absolute;right:0;top:0;width:265px;height:153px;
  background:linear-gradient(90deg,var(--blue) 0%,rgba(29,108,194,.55) 22%,#c9ddee 45%,#e9c7ad 65%,#b9cf9e 100%)}
.hero-notch{position:absolute;left:84px;top:-1px}
.hero-title{position:absolute;left:26px;top:62px;width:240px;color:#fff;font-weight:600;font-size:14.5px;line-height:18px;letter-spacing:.2px}
.section-head{border-left:5px solid var(--blue);padding-left:7px;font-weight:800;font-size:15px;line-height:15px;color:#1f1f1f;text-transform:uppercase;white-space:nowrap}
.section-head em{font-style:normal;color:var(--blue)}
.body-copy{font-size:7.6px;line-height:10.4px;color:var(--ink-soft)}
.body-copy p{margin-bottom:10px}
.body-copy .lead{color:var(--blue)}
.brand{left:52px;top:556px;width:178px;height:72px;display:flex;flex-direction:column;justify-content:center;align-items:flex-start}
.brand-name{display:flex;align-items:center;gap:6px;font-weight:800;font-size:25px;color:#1f1f1f;letter-spacing:.5px}
.brand-name span.mark{width:14px;height:14px;background:var(--blue)}
.brand-sub{font-size:8px;color:var(--blue);letter-spacing:.6px;margin-left:20px}
.footer-band{left:0;bottom:0;width:530px;height:40px;background:var(--blue);color:#fff;font-weight:600;font-size:11.5px;display:flex;align-items:center;justify-content:center}

/* back */
.feature-list{left:26px;top:172px;width:216px;list-style:none}
.feature-list li{font-size:10.3px;font-weight:600;color:var(--blue);height:19.2px;line-height:18px;border-bottom:1px solid var(--rule);padding-left:11px;position:relative}
.feature-list li::before{content:"";position:absolute;left:1px;top:7px;width:4.5px;height:4.5px;border-radius:50%;background:#8a8a8a}
.feature-list li span{font-weight:400}
.facts{left:26px;top:416px;width:250px;font-size:7.4px;line-height:9.4px;color:var(--ink-soft)}
.facts p{margin-bottom:9px}
.facts b{color:#222}
.url-pill{left:16px;top:643px;width:266px;height:20px;border-radius:10px;background:var(--blue);color:#fff;font-weight:600;font-size:9.4px;display:flex;align-items:center;justify-content:center}
.review-col{left:294px;top:0;width:236px;height:686px;background:var(--blue)}
.review-pointer{position:absolute;left:-1px;top:90px}
.quote-mark{position:absolute;left:46px;top:-30px;font-family:"Lora",serif;font-size:190px;line-height:1;color:var(--blue-deep);letter-spacing:-12px}
.review-title{position:absolute;left:49px;top:110px;color:#fff;font-weight:800;font-size:21px;line-height:19px}
.review{position:absolute;left:49px;width:170px;color:#fff;font-family:"Lora",serif;font-style:italic;font-size:8.5px;line-height:11.5px}
.review .by{margin-top:12px;font-size:9.5px}
.review-divider{position:absolute;left:40px;top:316px;width:178px;border-top:1px dashed rgba(255,255,255,.75)}
.contact-box{position:absolute;left:0;top:556px;width:236px;height:59px;background:var(--navy);color:#fff;font-weight:600;padding:6px 0 0 14px}
.contact-box .phone{font-size:21px;line-height:26px;display:flex;align-items:center;gap:6px}
.contact-box .web{font-size:17.5px;line-height:20px;display:flex;align-items:center;gap:6px}
.contact-box .icon{fill:#fff}
</style>
</head>
<body>

<section class="page page--front">
  <p class="abs intro">*Would you like to lower your monthly energy bill, enjoy a safer, more comfortable and durable home, and increase your homes appraisal value and sales appeal?</p>
  <div class="abs contact-top">
    <div class="phone"><svg width="9" height="9" viewBox="0 0 10 10"><path class="icon" d="M2 0.5l2 2.2-1 1.2c.6 1.3 1.6 2.3 2.9 2.9l1.2-1 2.2 2-1.2 1.7C4 9.4.6 6 .3 1.7z"/></svg>555-014-2290</div>
    <div class="web"><svg width="9" height="9" viewBox="0 0 10 10"><circle class="icon" cx="5" cy="5" r="4.6"/></svg>thermlioratings.com</div>
  </div>

  <div class="abs hero">
    <div class="hero-photo" role="img" aria-label="Photo of cupped hands holding a small paper house with an energy efficiency rating scale"></div>
    <svg class="hero-notch" width="84" height="44" viewBox="0 0 84 44"><path d="M0 0h84L48 40q-6 6-12 0z" fill="#fff"/></svg>
    <p class="hero-title">Then keep reading, because that is what a lost cost, home energy rating can do for you...</p>
  </div>

  <h2 class="abs section-head" style="left:24px;top:302px"><em>What</em> is a whole<br>home energy rating?</h2>
  <div class="abs body-copy" style="left:37px;top:356px;width:200px">
    <p class="lead">A Whole Home Energy Rating is a comprehensive evaluation of the efficiency of the entire home. You will receive a written report that includes a numeric score or “rating” of the home, plus recommendations for improvements that will reduce energy bills and make the home more comfortable.</p>
    <p>Each rating will receive an official California Home Energy Rating Certificate and home energy rating report with the California Energy Commission’s (CEC) seal. The report will identify the most cost-effective and appropriate energy efficiency improvements needed to save you money and provide long lasting comfort.</p>
  </div>

  <h2 class="abs section-head" style="left:272px;top:302px"><em>Who</em> needs a whole<br>home energy rating?</h2>
  <div class="abs body-copy" style="left:285px;top:358px;width:212px">
    <p>Everyone! Whether you are buying or selling, or plan on staying in your home for one year or the rest of your life, each whole home energy rating is geared toward helping you save money, and is custom tailored to fit your unique needs. The whole home energy rating can be designed to fit any lifestyle or energy improvement budget, with a focal point on cost effectiveness and common sense.</p>
    <p class="lead">Buyers who choose to get a whole home energy rating can better decide which home will save them money through energy efficiency! They may also be entitled to federal tax credits, and borrow up to $40,000 for energy improvements through their mortgage.</p>
    <p>Sellers who have a CEC certificate showing their homes energy efficiency ultimately make their homes more valuable and often sell their homes faster than those without documentation.</p>
    <p>Before you remodel your home, make sure you have a HERS Rater conduct a Whole Home Energy Rating so you know exactly where to focus your money.</p>
  </div>

  <div class="abs brand">
    <div class="brand-name"><span class="mark"></span>THERMLIO</div>
    <div class="brand-sub">ENERGY RATINGS</div>
  </div>

  <div class="abs footer-band">http://northfieldenergy.com/energy-audits/</div>
</section>

<section class="page page--back">
  <h2 class="abs section-head" style="left:17px;top:30px;line-height:18px;padding-top:2px;font-size:16.5px">Who <em>performs the</em><br><em>rating?</em></h2>
  <p class="abs body-copy" style="left:26px;top:76px;width:220px;font-size:7.4px;line-height:10.2px">A Home Energy Rating System (HERS) Rater, who is certified by the CEC will conduct the rating. Each California HERS Rater must follow standardized energy auditing procedures and use energy analysis software that meets CEC requirements.</p>
  <p class="abs" style="left:26px;top:134px;width:215px;font-size:7.4px;line-height:10.2px;font-weight:600;color:var(--blue)">The HERS Rater will inspect and assess all the major energy efficiency features of your home:</p>

  <ul class="abs feature-list">
    <li>Air leaks</li>
    <li>Cooling system</li>
    <li>Heating system</li>
    <li>Cooling/heating duct system</li>
    <li>Water heating system</li>
    <li>Insulation <span>(attic, walls, floor, roof)</span></li>
    <li>Windows</li>
    <li>Lighting</li>
    <li>Major appliances</li>
    <li>Solar <span>(if any)</span></li>
    <li>Other energy uses</li>
    <li>Prior energy bills</li>
  </ul>

  <div class="abs facts">
    <p>Every report is <b>custom tailore</b>d to each unique home.</p>
    <p>Thermlio Energy Ratings <b>includes a free duct leakage test and free building envelope leakage test</b> with each home energy audit.</p>
    <p><b>Heating and cooling ducts in an average California home leak almost 30 percent.</b> That is why when heating or cooling equipment is replaced, testing the system’s ducts for leaks is now required by building officials in many parts of the state.</p>
    <p>You wouldn’t buy a new car without knowing the “miles per gallon”, so <b>why buy a home without knowing the “home energy rating?”</b></p>
    <p>After your mortgage payment, your <b>energy bill is often the second largest monthly home ownership expense.</b></p>
    <p><b>Combine an Energy Efficient Mortgage (EEM) with other programs and you may be able to borrow up to $40,000</b> or more for efficiency improvements. Ask a knowledgeable lender if an EEM is right for you.</p>
  </div>

  <div class="abs url-pill">http://northfieldenergy.com/energy-audits/</div>

  <div class="abs review-col">
    <svg class="review-pointer" width="36" height="62" viewBox="0 0 36 62"><path d="M0 0L30 26q6 5 0 10L0 62z" fill="#fff"/></svg>
    <div class="quote-mark" aria-hidden="true">“</div>
    <h2 class="review-title">CUSTOMER<br>REVIEWS:</h2>
    <div class="review" style="top:178px">
      <p>“While having my air conditioning replaced, my ac contractor called this company to do the duct test. Mr. Dalton arrived right on time, and explained the process thoroughly. He was clean and efficient while working throughout the house. He put my mind at ease during the process. I would definitely recommend this company.”</p>
      <p class="by">-Jenna R.</p>
    </div>
    <div class="review-divider"></div>
    <div class="review" style="top:334px;font-size:8.4px">
      <p>“I had the pleasure of hiring Thermlio to perform a home energy audit on my home and I was truly amazed by the level of professionalism and the great service I received from Will Dalton. The audit report he provided me was very complete and informative. It allowed me to make informed financial decision regarding repairs to my home. After providing me the report he call me to explain everything in it and suggested various item to make my home more energy efficient. Mr. Dalton is a wealth of knowledge and I will highly recommend it to any homeowner.”</p>
      <p class="by" style="font-size:8.5px">-Marcus T.</p>
    </div>
    <div class="contact-box">
      <div class="phone"><svg width="12" height="12" viewBox="0 0 10 10"><path class="icon" d="M2 0.5l2 2.2-1 1.2c.6 1.3 1.6 2.3 2.9 2.9l1.2-1 2.2 2-1.2 1.7C4 9.4.6 6 .3 1.7z"/></svg>555-014-2290</div>
      <div class="web"><svg width="12" height="12" viewBox="0 0 10 10"><circle class="icon" cx="5" cy="5" r="4.6"/></svg>thermlioratings.com</div>
    </div>
  </div>
</section>

</body>
</html>
```